Food Safety 1-California workers only

3.25" by 4.5" Black and White Magazine Ad
This ad is to train California workers only.
Workers will be trained on: Food Safety, FSMA (Food Safety Modernization Act), using equipment safety, food processing production skills, worker safety, supervisory skills, communication skills.
"FREE TRAINING", The company does the training or Keystone Learning will provide the training.
Training grants range from $100,000 to $400,000.
Companies must be in business for profit.
Companies must train 200 employees or more.
This program is for California workers only.
Incumbent or new-hires are eligible.

Target Market(s)

California food processors, farms, food packaging, food processors, companies under FSMA, food safety, food production who need to train employees.

Industry/Entity Type

Food Production

Font styles to use
Serif
Sans Serif

Colors

Designer to choose colors to be used in the design.

Requirements
Must have
• This is a 3.25 inch by 4.5 inch magazine ad. It must be black and white. No color.
• The deliverable must be in basic PhotoShop. The ad does not need to include any graphics and be text only if needed. If you have a black and white graphic that will show well.
• Look at www.KLGFoodSafety..com
• Use the text from "MEALBOX-Photoshop-052018" file as your starting point.
Nice to have
• A black and white graphic about food. See www.KLGFoodSafety.com
Should not have
• No color.

```html
<!DOCTYPE html>
<html lang="en">
<head>
<meta charset="utf-8">
<title>Free Training – Food Safety Magazine Ad</title>
<link rel="stylesheet" href="https://fonts.googleapis.com/css2?family=Playfair+Display:wght@700;900&family=Oswald:wght@500;700&family=Open+Sans:wght@400;600;700&display=swap">
<style>
  :root {
    --backdrop: #e9e9e9;
    --paper: #ffffff;
    --ink: #1c1c1c;
    --charcoal: #4a4a4a;
    --slate: #5c5c5c;
    --mid-grey: #7d7d7d;
    --light-grey: #d8d8d8;
    --footer-text: #f2f2f2;
  }
  * { box-sizing: border-box; margin: 0; padding: 0; }
  html, body { width: 1200px; height: 1200px; overflow: hidden; }
  body {
    background: var(--backdrop);
    font-family: "Open Sans", Arial, sans-serif;
    color: var(--ink);
    position: relative;
  }
  .ad {
    position: absolute;
    left: 202px; top: 50px;
    width: 796px; height: 1100px;
    background: var(--paper);
    overflow: hidden;
    box-shadow: 0 2px 10px rgba(0,0,0,.15);
  }
  .ad-art { position: absolute; left: 0; top: 0; }

  .headline { position: absolute; left: 40px; top: 420px; width: 360px; }
  .headline-free {
    font-family: "Playfair Display", Georgia, serif;
    font-weight: 900;
    font-size: 96px;
    line-height: .9;
    color: var(--mid-grey);
    letter-spacing: 2px;
  }
  .headline-training {
    font-family: "Playfair Display", Georgia, serif;
    font-weight: 900;
    font-size: 50px;
    line-height: 1;
    color: var(--ink);
    letter-spacing: 1px;
    margin-top: 2px;
  }
  .headline-topic {
    font-family: "Oswald", Arial, sans-serif;
    font-weight: 700;
    font-size: 40px;
    line-height: 1.05;
    color: var(--slate);
    margin-top: 8px;
  }
  .headline-skills {
    font-family: "Oswald", Arial, sans-serif;
    font-weight: 700;
    font-size: 20px;
    line-height: 1.3;
    color: var(--ink);
    letter-spacing: .3px;
  }
  .pitch {
    font-size: 24px;
    line-height: 1.2;
    color: var(--charcoal);
    margin-top: 10px;
  }
  .pitch-or { font-weight: 700; color: var(--ink); margin-top: 4px; }
  .pitch-alt { margin-top: 4px; }

  .contact-pill {
    margin-top: 16px;
    width: 270px;
    padding: 10px 20px;
    border: 2px solid var(--light-grey);
    border-radius: 16px;
    background: var(--paper);
    box-shadow: 0 3px 8px rgba(0,0,0,.18);
    font-weight: 700;
  }
  .contact-name { font-size: 21px; letter-spacing: .5px; color: var(--ink); }
  .contact-phone { font-size: 21px; color: var(--charcoal); display: flex; align-items: center; gap: 8px; }

  .qualify-panel {
    position: absolute;
    left: 420px; top: 385px;
    width: 350px; height: 460px;
    background: var(--slate);
    border-radius: 18px;
    padding: 30px 26px;
    color: var(--footer-text);
    box-shadow: 0 4px 10px rgba(0,0,0,.25);
  }
  .qualify-title { font-size: 26px; font-weight: 700; color: #fff; margin-bottom: 14px; }
  .qualify-list { list-style: none; font-size: 17px; line-height: 1.35; }
  .qualify-list li { position: relative; padding-left: 20px; margin-bottom: 10px; }
  .qualify-list li::before {
    content: ""; position: absolute; left: 2px; top: 9px;
    width: 7px; height: 7px; border-radius: 50%; background: var(--footer-text);
  }

  .footer-band {
    position: absolute;
    left: 18px; right: 18px; bottom: 18px;
    height: 170px;
    background: var(--slate);
    color: var(--footer-text);
  }
  .company-address {
    position: absolute; left: 30px; bottom: 22px;
    display: flex; gap: 10px; font-size: 18px; line-height: 1.3;
  }
  .web-links {
    position: absolute; left: 420px; top: 20px;
    list-style: none; font-size: 18px; line-height: 1.7;
  }
  .web-links li { display: flex; align-items: center; gap: 10px; }
  .icon { flex: none; }
</style>
</head>
<body>
  <main class="ad">
    <svg class="ad-art" width="796" height="1100" viewBox="0 0 796 1100">
      <defs>
        <linearGradient id="produce-tone" x1="0" y1="0" x2="1" y2="1">
          <stop offset="0" stop-color="#d6d6d6"/>
          <stop offset=".55" stop-color="#8a8a8a"/>
          <stop offset="1" stop-color="#5a5a5a"/>
        </linearGradient>
        <radialGradient id="crate-tone" cx=".45" cy=".4" r=".7">
          <stop offset="0" stop-color="#9a9a9a"/>
          <stop offset="1" stop-color="#cfcfcf"/>
        </radialGradient>
      </defs>
      <rect x="0" y="0" width="796" height="1100" fill="var(--paper)"/>
      <path role="img" aria-label="Photo of fresh vegetables and produce"
            d="M18 18 H778 V250 C620 330 360 380 18 380 Z" fill="url(#produce-tone)"/>
      <path d="M18 396 C360 396 620 348 790 262" fill="none" stroke="var(--slate)" stroke-width="12"/>
      <path d="M18 410 C360 410 630 362 790 278" fill="none" stroke="var(--light-grey)" stroke-width="4"/>
      <circle cx="630" cy="220" r="128" fill="var(--paper)" stroke="var(--slate)" stroke-width="6"/>
      <circle role="img" aria-label="Photo of a crate of leafy greens and carrots" cx="630" cy="220" r="114" fill="url(#crate-tone)"/>
    </svg>

    <section class="headline">
      <div class="headline-free">FREE</div>
      <div class="headline-training">TRAINING</div>
      <div class="headline-topic">FOOD SAFETY FSMA</div>
      <div class="headline-skills">PRODUCTION SKILLS WORKER SAFETY</div>
      <p class="pitch">You do the training and the state of california pays for it!</p>
      <p class="pitch pitch-or">or</p>
      <p class="pitch pitch-alt">We do the training and the state pays for it!</p>
      <div class="contact-pill">
        <div class="contact-name">DANIEL MARSH</div>
        <div class="contact-phone">
          <svg class="icon" width="20" height="20" viewBox="0 0 20 20"><circle cx="10" cy="10" r="10" fill="var(--charcoal)"/><path d="M6.5 5.5l2 2-1 1.3c.6 1.4 1.8 2.6 3.2 3.2l1.3-1 2 2-1.2 1.5c-3.5-.4-7.3-4.2-7.7-7.7z" fill="#fff"/></svg>
          (555) 014-2290
        </div>
      </div>
    </section>

    <aside class="qualify-panel">
      <h2 class="qualify-title">How to qualify</h2>
      <ul class="qualify-list">
        <li>Train California Workers Only</li>
        <li>Trainees must earn $11/hour</li>
        <li>Full-time workers only</li>
        <li>Employees must attend at least 8 Hours of training</li>
        <li>You must train 200 or more employees</li>
        <li>Incumbent or New-Hire workers are eligible</li>
        <li>Seasonal workers are eligible</li>
      </ul>
    </aside>

    <footer class="footer-band">
      <div class="company-address">
        <svg class="icon" width="16" height="22" viewBox="0 0 16 22"><path d="M8 0a8 8 0 0 0-8 8c0 6 8 14 8 14s8-8 8-14a8 8 0 0 0-8-8zm0 11a3 3 0 1 1 0-6 3 3 0 0 1 0 6z" fill="#f2f2f2"/></svg>
        <p>Keystone Learning Company, Inc<br>1200 Orchard Lane, Suite 310<br>Fairview, CA 90000</p>
      </div>
      <ul class="web-links">
        <li><svg class="icon" width="18" height="18" viewBox="0 0 18 18"><circle cx="9" cy="9" r="8" fill="none" stroke="#f2f2f2" stroke-width="1.6"/><path d="M1 9h16M9 1c-4 4-4 12 0 16M9 1c4 4 4 12 0 16" fill="none" stroke="#f2f2f2" stroke-width="1.3"/></svg>www.KLGCAL.com</li>
        <li><svg class="icon" width="18" height="18" viewBox="0 0 18 18"><circle cx="9" cy="9" r="8" fill="none" stroke="#f2f2f2" stroke-width="1.6"/><path d="M1 9h16M9 1c-4 4-4 12 0 16M9 1c4 4 4 12 0 16" fill="none" stroke="#f2f2f2" stroke-width="1.3"/></svg>www.KLGFoodSafety.com</li>
        <li><svg class="icon" width="18" height="14" viewBox="0 0 18 14"><rect x="0" y="0" width="18" height="14" rx="2" fill="#f2f2f2"/><path d="M1 1l8 7 8-7" fill="none" stroke="var(--slate)" stroke-width="1.6"/></svg>dan.marsh@KLGCAL.com</li>
      </ul>
    </footer>
  </main>
</body>
</html>
```